Upstart Retirement Planning Firm needs help with business card design

Harborlight Wealth Partners, LLC is looking for help with business card design. We give advice on investments, insurance, and other financial matters related to retirement. There are some required disclosures that we will provide but mostly we are looking for a professional, classy business card that reflects the theme we have chosen. We have a logo that is attached but we would like to add a phrase; "Turning Your Earned Income Into Retirement Income"

Doubled sided only so that we can add the required disclosures (needed for our industry) on the back of the card. We will provide the exact words for this in 1-2 days.

Target Market(s)

Retirees and Pre-retirees. Professionals 50+ years old

Industry/Entity Type

Financial Planning

Contact Information for Business Card

We currently have two people who will need separate cards so we'd like to have a template so that we can add names for new cards in the future.

For the first run, please show the following information.

Neil Osgood, MBA, ChFC®, CLU®
Financial Advisor, Registered Representative
nosgood@harborlightwp.example
Phone: (555) 218-3960
Toll Free Fax: (555) 218-3961

Address is
2876 Meadowbrook Pkwy.
Suite K418
Virginia Beach, VA 23019

Colors
3277b5

Requirements
Must have
• Logo, contact info, small phase to describe business (in description), required legal disclosures on back of the card as follows (in small font)
• Neil Osgood is a registered representative of and offers securities through Brightwater Capital Brokerage Corporation, Member SIPC. Brightwater Capital Brokerage Corporation is a member of the Brightwater Advisory Group which is the marketing name for Brightwater Holding Corporation and its affiliates.
Nice to have
• Rounded edges, raised letters
Should not have
• any colors that aren't in the logo (other than black for font)

```html
<!DOCTYPE html>
<html lang="en">
<head>
<meta charset="utf-8">
<title>Harborlight Wealth Partners — Business Card</title>
<link href="https://fonts.googleapis.com/css2?family=Open+Sans:wght@400;600;700&display=swap" rel="stylesheet">
<style>
  :root {
    --backdrop: #2e2825;
    --brand-blue: #3277b5;
    --brand-blue-deep: #1f5a9c;
    --brand-blue-light: #4a8fcc;
    --ink-white: #ffffff;
    --silver: #dfe6ee;
  }
  * { margin: 0; padding: 0; box-sizing: border-box; }
  html, body {
    width: 1200px; height: 844px; overflow: hidden;
    background: var(--backdrop);
    font-family: "Open Sans", Arial, sans-serif;
  }
  .canvas {
    position: relative; width: 1200px; height: 844px;
    display: flex; align-items: center; justify-content: center; gap: 60px;
  }
  .card {
    position: relative; width: 520px; height: 297px;
    border-radius: 12px; overflow: hidden;
    background: radial-gradient(ellipse at 40% 35%, var(--brand-blue-light) 0%, var(--brand-blue) 45%, var(--brand-blue-deep) 100%);
    color: var(--ink-white);
    box-shadow: 0 10px 30px rgba(0,0,0,.45);
  }

  /* Front: contact side */
  .card-front .brand-mark {
    position: absolute; left: 30px; top: 92px; width: 170px;
    display: flex; align-items: center; gap: 8px;
    font-size: 15px; font-weight: 600; line-height: 1.25; color: var(--silver);
  }
  .brand-mark .dot {
    flex: 0 0 14px; width: 14px; height: 14px; border-radius: 50%;
    background: var(--silver);
  }
  .contact {
    position: absolute; left: 228px; top: 62px; right: 18px;
    font-size: 13px; line-height: 1.5;
  }
  .contact .name { font-size: 17px; font-weight: 700; }
  .contact .name .creds { font-size: 12px; font-weight: 600; }
  .contact .title { font-size: 12.5px; margin-bottom: 10px; }
  .contact .line { display: flex; align-items: center; gap: 6px; }
  .contact .line svg { width: 11px; height: 11px; fill: var(--ink-white); flex: 0 0 11px; }
  .contact .fax { font-weight: 700; font-size: 12.5px; letter-spacing: .2px; }
  .contact .address { margin-top: 14px; }

  /* Back: brand side */
  .card-back {
    display: flex; flex-direction: column; align-items: center; justify-content: center;
  }
  .card-back .brand-mark {
    display: flex; align-items: center; gap: 10px;
    font-size: 22px; font-weight: 600; color: var(--silver);
  }
  .card-back .rule {
    width: 330px; height: 2px; background: var(--ink-white); margin: 14px 0 12px;
  }
  .card-back .tagline {
    font-size: 15px; font-weight: 600; color: var(--ink-white);
  }
</style>
</head>
<body>
<main class="canvas">

  <section class="card card-front" aria-label="Business card front">
    <div class="brand-mark"><span class="dot"></span><span>Harborlight Wealth Partners, LLC</span></div>
    <div class="contact">
      <p class="name">Neil Osgood, MBA, <span class="creds">ChFC®, CLU®</span></p>
      <p class="title">Financial Advisor, Registered Representative</p>
      <p class="line">
        <svg viewBox="0 0 24 24" aria-hidden="true"><path d="M6.6 10.8a15.1 15.1 0 0 0 6.6 6.6l2.2-2.2a1 1 0 0 1 1-.25 11.4 11.4 0 0 0 3.6.57 1 1 0 0 1 1 1V20a1 1 0 0 1-1 1A17 17 0 0 1 3 4a1 1 0 0 1 1-1h3.5a1 1 0 0 1 1 1c0 1.25.2 2.45.57 3.6a1 1 0 0 1-.25 1z"/></svg>
        (555) 218-3960
      </p>
      <p class="line">
        <svg viewBox="0 0 24 24" aria-hidden="true"><path d="M2 5h20v14H2z M2 5l10 8 10-8" fill="none" stroke="#fff" stroke-width="0"/><path d="M2 5h20v2l-10 7L2 7zM2 9l10 7 10-7v10H2z"/></svg>
        nosgood@harborlightwp.example
      </p>
      <p class="fax">TOLL FREE FAX: (555) 218-3961</p>
      <p class="address">2876 Meadowbrook Pkwy. Suite<br>K418 Virginia Beach, VA 23019</p>
    </div>
  </section>

  <section class="card card-back" aria-label="Business card back">
    <div class="brand-mark"><span>Harborlight Wealth Partners, LLC</span></div>
    <div class="rule"></div>
    <p class="tagline">Turning Your Earned Income Into Retirement Income</p>
  </section>

</main>
</body>
</html>
```